Designing a website for Korvale Pest Solutions PTY LTD

Pest control company looking for someone to build an informative website containing services we offer and an online inquiry form.
Commercial premises - Specialising in - Rodent control, stored product pest control, flying insect control, ant, spider and insect control, Termite inspections and treatments. Termite management systems on a commercial scale.
Facilities we service
Commercial - shopping centres, transport facilities, restaurants, pubs, clubs, bars food manufacturing facilities.
Residential - Houses specialising in - Rodent, Ant, Spider, Cockroach and Termite control. Termite inspections, Pre - purchase inspections, Termite treatments, Termite management systems.
Target Market(s)
Mainly commercial and industrial clients and Residential clients.
Industry/Entity Type
Pest Control
Number of Pages Required
1 page
Look and feel
Each slider illustrates characteristics of the customer's brand and the style your logo design should communicate.

```html
<!DOCTYPE html>
<html lang="en">
<head>
<meta charset="utf-8">
<title>Korvale Pest Solutions</title>
<link href="https://fonts.googleapis.com/css2?family=Roboto:wght@400;500;700&display=swap" rel="stylesheet">
<style>
:root{
  --green:#3b8c12;
  --green-dark:#2f7409;
  --ink:#222;
  --text:#444;
  --muted:#8a8a8a;
  --soft:#f5f5f5;
  --line:#e6e6e6;
  --footer:#2f2f2f;
  --white:#fff;
}
*{box-sizing:border-box;margin:0;padding:0}
html,body{width:1200px;height:3960px;overflow:hidden}
body{font-family:'Roboto',sans-serif;color:var(--ink);background:var(--white);position:relative}
a{color:inherit;text-decoration:none}
section,header,footer{position:absolute;left:0;width:1200px}
.label{font-size:14px;letter-spacing:2px;color:var(--green);font-weight:500;text-transform:uppercase}
.title{font-size:30px;font-weight:500;color:var(--ink)}
.center{text-align:center}
.btn{display:inline-flex;align-items:center;justify-content:center;font-size:14px;font-weight:500;height:46px;border:2px solid var(--green)}
.btn-solid{background:var(--green);color:#fff}
.btn-line{background:#fff;color:var(--ink)}
.arrow{display:inline-block;vertical-align:middle}

/* nav */
.nav{top:0;height:68px;background:#fff;border-bottom:1px solid var(--line)}
.brand{position:absolute;left:148px;top:20px;display:flex;align-items:center;gap:8px;font-size:20px;font-weight:700;color:var(--ink)}
.brand i{width:14px;height:14px;border-radius:50%;background:var(--green);display:block}
.menu{position:absolute;right:152px;top:0;display:flex;gap:38px;height:68px;align-items:center;font-size:14px;font-weight:500}
.menu a{height:68px;display:flex;align-items:center}
.menu .active{color:var(--green)}
.menu .hover{border-bottom:3px solid var(--green)}

/* hero */
.hero{top:68px;height:524px;background:linear-gradient(90deg,#141a1e 0%,#1d2529 55%,#2a3338 100%)}
.hero-photo{position:absolute;right:0;top:0;width:600px;height:524px;background:radial-gradient(ellipse at 55% 55%,#c9d3dc 0%,#8c9aa6 40%,#2a3338 75%)}
.hero h1{position:absolute;left:148px;top:145px;color:#fff;font-size:37px;line-height:53px;font-weight:700}
.hero p{position:absolute;left:148px;top:262px;width:400px;color:#d8d8d8;font-size:14px;line-height:22px}
.hero .actions{position:absolute;left:148px;top:327px;display:flex;gap:24px}
.hero .btn{width:172px;height:48px}
.hero .btn-line{border-color:#fff}

/* services */
.services{top:592px;height:519px}
.services .label{position:absolute;top:50px;width:100%}
.services .title{position:absolute;top:72px;width:100%}
.card{position:absolute;width:275px;height:137px;background:#fff;box-shadow:0 2px 10px rgba(0,0,0,.12);padding:18px 22px}
.card h3{font-size:14px;font-weight:500;margin-top:12px}
.card .more{display:flex;align-items:center;gap:8px;color:var(--green);font-size:14px;font-weight:500;margin-top:14px}

/* features */
.features{top:1111px;height:441px;background:var(--soft)}
.feat-frame{position:absolute;left:148px;top:37px;width:210px;height:367px;background:var(--green);border-radius:12px 0 0 12px}
.feat-photo{position:absolute;left:164px;top:53px;width:374px;height:337px;border-radius:10px;background:linear-gradient(160deg,#5c8a3a,#8fb35e 45%,#3f6b22);box-shadow:0 4px 12px rgba(0,0,0,.2)}
.features .label{position:absolute;left:613px;width:360px;top:47px;text-align:center}
.features .title{position:absolute;left:613px;top:66px}
.feat{position:absolute;left:613px;display:flex;align-items:center;gap:22px;font-size:18px;font-weight:500}
.feat .ico{width:50px;height:50px;background:var(--green);display:flex;align-items:center;justify-content:center}
.features .btn{position:absolute;left:613px;top:358px;width:166px;height:46px}

/* facilities */
.facilities{top:1552px;height:1060px}
.facilities .label{position:absolute;top:52px;width:100%}
.facilities .title{position:absolute;top:72px;width:100%}
.tabs{position:absolute;top:129px;width:100%;display:flex;justify-content:center;gap:38px;font-size:18px;color:var(--muted)}
.tabs .on{color:var(--green);font-weight:500}
.tabs span.sep{width:1px;height:22px;background:#ccc}
.fac{position:absolute;width:276px;height:335px}
.fac .img{width:276px;height:263px}
.fac .tag{position:absolute;left:20px;top:226px;width:233px;height:108px;background:#fff;box-shadow:0 2px 10px rgba(0,0,0,.1);padding:14px 16px}
.fac .tag small{display:block;font-size:17px;color:var(--muted)}
.fac .tag b{display:block;font-size:20px;font-weight:500;margin-top:6px}
.fac .tag svg{margin-top:10px}
.view-all{position:absolute;left:545px;top:962px;width:108px;height:44px;font-size:14px}

/* testimonials */
.testimonials{top:2612px;height:443px;background:var(--soft)}
.testimonials .label{position:absolute;top:45px;width:100%}
.testimonials .title{position:absolute;top:66px;width:100%}
.quote{position:absolute;top:138px;width:411px;height:215px;border:2px solid var(--green);border-top-color:transparent;border-radius:0 0 8px 8px}
.quote:before{content:"";position:absolute;left:0;right:0;top:0;border-top:2px solid var(--green)}
.quote .q{position:absolute;top:-23px;left:52px;width:54px;height:54px;background:var(--green);display:flex;align-items:center;justify-content:center;color:#fff;font-size:40px;font-weight:700;font-family:Georgia,serif;line-height:1}
.quote p{position:absolute;left:38px;top:42px;width:350px;font-size:14px;line-height:22px;color:var(--ink)}
.who{position:absolute;left:38px;top:128px;display:flex;align-items:center;gap:16px}
.avatar{width:62px;height:56px;background:linear-gradient(135deg,#b9b0a6,#7b736c)}
.who b{display:block;font-size:13px;font-weight:400}
.who small{display:block;font-size:12px;color:var(--green);margin-top:8px}
.pager{position:absolute;top:400px;width:100%;display:flex;justify-content:center;align-items:center;gap:10px}
.dot{width:14px;height:14px;border-radius:50%;border:2px solid var(--green)}
.dot.on{background:var(--green)}

/* quote */
.request{top:3055px;height:602px}
.request .label{position:absolute;left:150px;width:420px;text-align:center;top:58px}
.request .title{position:absolute;left:150px;top:85px;font-size:30px;line-height:46px;width:440px}
.request .lead{position:absolute;left:150px;top:183px;width:400px;font-size:14px;line-height:23px;color:var(--ink)}
.request .actions{position:absolute;left:150px;top:264px;display:flex;gap:22px}
.request .btn{width:150px;height:44px}
.kind{position:absolute;top:362px;width:200px}
.kind h4{font-size:14px;font-weight:500;margin-top:16px}
.kind p{font-size:12px;line-height:20px;color:var(--text);margin-top:6px}
.kind a{display:flex;align-items:center;gap:6px;color:var(--green);font-size:14px;font-weight:500;margin-top:8px}
.form{position:absolute;left:641px;top:53px;width:408px;height:495px;background:#fff;box-shadow:0 2px 14px rgba(0,0,0,.12);padding:36px 22px}
.form h3{font-size:18px;font-weight:500}
.form .intro{font-size:13px;line-height:22px;color:var(--muted);margin-top:12px}
.grid{display:grid;grid-template-columns:170px 170px;column-gap:22px;row-gap:18px;margin-top:16px}
.field label{display:block;font-size:12px;margin-bottom:10px}
.field .box{height:36px;background:#f0f0f0;display:flex;align-items:center;padding:0 14px;font-size:12px;color:var(--muted);justify-content:space-between}
.checks{display:flex;gap:24px;font-size:12px;margin-top:18px;align-items:center}
.checks span{display:flex;align-items:center;gap:7px}
.cb{width:11px;height:11px;border:1.5px solid #333;display:inline-block}
.cb.on{background:var(--green);border-color:#333;box-shadow:inset 0 0 0 2px #fff}
.submit{margin-top:20px;height:36px;background:var(--green);color:#fff;font-size:14px;font-weight:500;display:flex;align-items:center;justify-content:center}

/* footer */
.footer{top:3657px;height:303px;background:var(--footer);color:#e9e9e9}
.col{position:absolute;top:40px}
.col h5{color:var(--green);font-size:15px;font-weight:500;margin-bottom:22px}
.col li{list-style:none;font-size:14px;margin-bottom:14px;display:flex;align-items:center;gap:8px}
.socials{display:flex;gap:16px;margin-top:4px}
.socials i{width:8px;height:8px;border-radius:50%;background:#e9e9e9;display:block}
.news p{font-size:14px;line-height:22px;width:230px}
.subscribe{margin-top:20px;width:228px;height:40px;border:1px solid #ddd;display:flex}
.subscribe span{flex:1;font-size:11px;display:flex;align-items:center;padding-left:20px}
.subscribe b{width:40px;background:#fff;display:flex;align-items:center;justify-content:center}
.rule{position:absolute;left:150px;right:150px;top:257px;border-top:1px solid #4a4a4a}
.copy{position:absolute;top:274px;width:100%;text-align:center;font-size:12px}
</style>
</head>
<body>

<header class="nav">
  <div class="brand"><i></i>Korvale</div>
  <nav class="menu">
    <a class="active">Home</a><a>Services</a><a class="hover">Company</a><a>Commercial</a><a>Residential</a><a>Pricing</a><a>Contact Us</a>
  </nav>
</header>

<section class="hero">
  <div class="hero-photo" role="img" aria-label="Technician in white protective suit and respirator holding a spray wand"></div>
  <h1>Best 360 degree solutions<br>for your pest problem.</h1>
  <p>Lorem ipsum dolor sit amet, consetetur sadipscing elitr, sed diam nonumy eirmod tempor invidunt ut labore et dolore</p>
  <div class="actions">
    <a class="btn btn-solid">Get a Free Quote</a>
    <a class="btn btn-line">Our Services</a>
  </div>
</section>

<svg width="0" height="0" style="position:absolute">
  <defs>
    <symbol id="bug" viewBox="0 0 40 40">
      <g fill="none" stroke="#222" stroke-width="1.6" stroke-linecap="round">
        <ellipse cx="20" cy="24" rx="9" ry="10"/>
        <circle cx="20" cy="11" r="4"/>
        <path d="M17 8l-4-5M23 8l4-5M11 20l-8-4M11 26H2M12 31l-7 5M29 20l8-4M29 26h9M28 31l7 5M20 15v19"/>
      </g>
    </symbol>
    <symbol id="arr" viewBox="0 0 20 16">
      <path d="M1 8h16M11 2l6 6-6 6" fill="none" stroke="#3b8c12" stroke-width="2.6" stroke-linecap="round" stroke-linejoin="round"/>
    </symbol>
  </defs>
</svg>

<section class="services">
  <div class="label center">Our Services</div>
  <h2 class="title center">Solutions to your every Problem</h2>
  <div class="card" style="left:148px;top:158px"><svg width="40" height="40"><use href="#bug"/></svg><h3>General Pest Control</h3><a class="more">Know More <svg width="20" height="16"><use href="#arr"/></svg></a></div>
  <div class="card" style="left:459px;top:158px"><svg width="40" height="40"><use href="#bug"/></svg><h3>Rodent &nbsp;Control</h3><a class="more">Know More <svg width="20" height="16"><use href="#arr"/></svg></a></div>
  <div class="card" style="left:771px;top:158px"><svg width="40" height="40"><use href="#bug"/></svg><h3>Stored Product Pest Control</h3><a class="more">Know More <svg width="20" height="16"><use href="#arr"/></svg></a></div>
  <div class="card" style="left:148px;top:330px"><svg width="40" height="40"><use href="#bug"/></svg><h3>Flying Insect Control</h3><a class="more">Know More <svg width="20" height="16"><use href="#arr"/></svg></a></div>
  <div class="card" style="left:459px;top:330px"><svg width="40" height="40"><use href="#bug"/></svg><h3>Ant, Spiders, and Insect Control</h3><a class="more">Know More <svg width="20" height="16"><use href="#arr"/></svg></a></div>
  <div class="card" style="left:771px;top:330px"><svg width="40" height="40"><use href="#bug"/></svg><h3>Termite Inspection and Treatment</h3><a class="more">Know More <svg width="20" height="16"><use href="#arr"/></svg></a></div>
</section>

<section class="features">
  <div class="feat-frame"></div>
  <div class="feat-photo" role="img" aria-label="Family kneeling on a lawn with their dog"></div>
  <div class="label">Features</div>
  <h2 class="title">Best Features only for You</h2>
  <div class="feat" style="top:116px"><span class="ico"><svg width="20" height="20" viewBox="0 0 20 20"><path d="M3 17C3 8 9 4 17 3c-1 8-5 13-13 13M4 16l8-8" fill="#fff" stroke="#fff" stroke-width="1.2"/></svg></span>Eco Friendly Service</div>
  <div class="feat" style="top:196px"><span class="ico"><svg width="20" height="20" viewBox="0 0 20 20"><circle cx="12" cy="7" r="4" fill="#fff"/><path d="M3 17v-6h4v6z" fill="#fff"/></svg></span>Family Owned</div>
  <div class="feat" style="top:285px"><span class="ico"><svg width="22" height="18" viewBox="0 0 22 18"><circle cx="11" cy="5" r="3" fill="#fff"/><circle cx="4" cy="7" r="2.3" fill="#fff"/><circle cx="18" cy="7" r="2.3" fill="#fff"/><path d="M5 16a6 6 0 0 1 12 0zM0 16a4 4 0 0 1 6-3v3zM22 16a4 4 0 0 0-6-3v3z" fill="#fff"/></svg></span>Expert Team and Professionals</div>
  <a class="btn btn-solid">Get a Free Quote</a>
</section>

<section class="facilities">
  <div class="label center">Facilities</div>
  <h2 class="title center">Facilities We Service</h2>
  <div class="tabs"><span class="on">ALL</span><span class="sep"></span><span>RESIDENTIAL</span><span class="sep"></span><span>COMMERCIAL</span></div>

  <div class="fac" style="left:148px;top:204px"><div class="img" role="img" aria-label="Close-up of a termite on timber" style="background:linear-gradient(160deg,#c98f4a,#e5c08a 50%,#8a5a2a)"></div><div class="tag"><small>Residential</small><b>Termite Treatments</b><svg width="20" height="16"><use href="#arr"/></svg></div></div>
  <div class="fac" style="left:460px;top:204px"><div class="img" role="img" aria-label="Busy restaurant terrace with hanging greenery" style="background:linear-gradient(180deg,#4e7a3a,#8d9a88 50%,#4a4a48)"></div><div class="tag"><small>Commercial</small><b>Restaurants</b><svg width="20" height="16"><use href="#arr"/></svg></div></div>
  <div class="fac" style="left:773px;top:204px"><div class="img" role="img" aria-label="Cockroaches on a wooden surface" style="background:linear-gradient(170deg,#c99e68,#a2703a 55%,#3d2a16)"></div><div class="tag"><small>Residential</small><b>Coackroaches</b><svg width="20" height="16"><use href="#arr"/></svg></div></div>

  <div class="fac" style="left:148px;top:576px"><div class="img" role="img" aria-label="Crowd at a nightclub under green lights" style="background:radial-gradient(ellipse at 50% 30%,#a6f06a,#2e9a1c 45%,#0b1d08)"></div><div class="tag"><small>Commercial</small><b>Pubs and Clubs</b><svg width="20" height="16"><use href="#arr"/></svg></div></div>
  <div class="fac" style="left:460px;top:576px"><div class="img" role="img" aria-label="Ants gathered around food crumbs" style="background:radial-gradient(ellipse at 50% 55%,#d4b08a,#d9d3cc 50%,#bfb8b0)"></div><div class="tag"><small>Residential</small><b>Ants and Insects</b><svg width="20" height="16"><use href="#arr"/></svg></div></div>
  <div class="fac" style="left:773px;top:576px"><div class="img" role="img" aria-label="Multi-level shopping centre interior" style="background:linear-gradient(180deg,#7a8fa0,#c8c4bb 45%,#5d8a90)"></div><div class="tag"><small>Commercial</small><b>Shopping Centres</b><svg width="20" height="16"><use href="#arr"/></svg></div></div>

  <a class="btn btn-line view-all">View All</a>
</section>

<section class="testimonials">
  <div class="label center">Testimonials</div>
  <h2 class="title center">What our Customers say about Us</h2>
  <div class="quote" style="left:149px">
    <span class="q">“</span>
    <p>Lorem ipsum dolor sit amet, consetetur sadipscing elitr, sed diam nonumy eirmod tempor invidunt ut labore et dolore magna aliquyam erat, sed diam.</p>
    <div class="who"><div class="avatar" role="img" aria-label="Customer portrait"></div><div><b>Daniel Hartwell</b><small>CEO of Brightmoor Foods</small></div></div>
  </div>
  <div class="quote" style="left:638px">
    <span class="q">“</span>
    <p>Lorem ipsum dolor sit amet, consetetur sadipscing elitr, sed diam nonumy eirmod tempor invidunt ut labore et dolore magna aliquyam erat, sed diam.</p>
    <div class="who"><div class="avatar" role="img" aria-label="Customer portrait"></div><div><b>Maya Ostrand</b><small>HouseWife</small></div></div>
  </div>
  <div class="pager">
    <svg width="22" height="16" viewBox="0 0 20 16" style="transform:scaleX(-1);margin-right:30px"><use href="#arr"/></svg>
    <span class="dot on"></span><span class="dot"></span><span class="dot"></span>
    <svg width="22" height="16" viewBox="0 0 20 16" style="margin-left:30px"><use href="#arr"/></svg>
  </div>
</section>

<section class="request">
  <div class="label">Quote</div>
  <h2 class="title">You Deserve a Clean, Safe, and Healthy Environment</h2>
  <p class="lead">For a cleaning that meets your highest standards, you need a dedicated team of trained specialists with all supplies needed to thoroughly clean your home and work place.</p>
  <div class="actions"><a class="btn btn-solid">Explore More</a><a class="btn btn-line">Our Services</a></div>

  <div class="kind" style="left:150px">
    <svg width="52" height="48" viewBox="0 0 52 48" fill="none" stroke="#222" stroke-width="1.6"><path d="M2 20L26 3l24 17M7 17v29h38V17M13 27h9v19h-9zM29 27h11v9H29zM34 27v9M29 31h11M34 8v6h5v-3"/></svg>
    <h4>Residential Cleaning</h4>
    <p>Lorem ipsum dolor sit amet, amt labore et dolore magna aliquyam erat, sed diam.</p>
    <a>Know More <svg width="16" height="13"><use href="#arr"/></svg></a>
  </div>
  <div class="kind" style="left:384px">
    <svg width="52" height="48" viewBox="0 0 52 48" fill="none" stroke="#222" stroke-width="1.6"><path d="M6 14h40l-4-10H10zM6 14v5a5 5 0 0 0 10 0 5 5 0 0 0 10 0 5 5 0 0 0 10 0 5 5 0 0 0 10 0v-5M9 24v22h34V24M14 30h10v16H14zM29 30h9v8h-9zM16 4l-2 10M26 4v10M36 4l2 10"/></svg>
    <h4>Commercial Cleaning</h4>
    <p>Lorem ipsum dolor sit amet, amt labore et dolore magna aliquyam erat, sed diam.</p>
    <a>Know More <svg width="16" height="13"><use href="#arr"/></svg></a>
  </div>

  <form class="form">
    <h3>Get a Quote</h3>
    <p class="intro">Lorem ipsum dolor sit amet, consetetur sadipscing amt labore et dolore magna aliquyam erat, sed diam.</p>
    <div class="grid">
      <div class="field"><label>Name</label><div class="box">|</div></div>
      <div class="field"><label>Phone</label><div class="box">|</div></div>
      <div class="field"><label>Address</label><div class="box">|</div></div>
      <div class="field"><label>Email</label><div class="box">|</div></div>
      <div class="field"><label>Choose your Service</label><div class="box">Termites <svg width="10" height="6"><path d="M1 1l4 4 4-4" fill="none" stroke="#888"/></svg></div></div>
      <div class="field"><label>Indicate Type of Cleaning</label><div class="box">Weekly <svg width="10" height="6"><path d="M1 1l4 4 4-4" fill="none" stroke="#888"/></svg></div></div>
    </div>
    <div class="checks"><span><i class="cb on"></i>Residential</span><span><i class="cb"></i>Commercial</span></div>
    <div class="submit">Submit</div>
  </form>
</section>

<footer class="footer">
  <div class="col" style="left:150px">
    <h5>Support</h5>
    <ul><li>Privacy Policy</li><li>Terms &amp; Conditions</li></ul>
    <div class="socials"><i></i><i></i><i></i><i></i></div>
  </div>
  <div class="col" style="left:369px">
    <h5>Company</h5>
    <ul><li>About</li><li>Services</li><li>Commercial</li><li>Residential</li><li>Pricing</li></ul>
  </div>
  <div class="col" style="left:537px">
    <h5>Contact Us</h5>
    <ul>
      <li><svg width="14" height="14" viewBox="0 0 14 14"><path d="M3 1l3 3-2 2a8 8 0 0 0 4 4l2-2 3 3-2 2C5 13 1 9 1 3z" fill="#fff"/></svg>+1800 0410 7723</li>
      <li><svg width="14" height="11" viewBox="0 0 14 11"><rect width="14" height="11" fill="#fff"/><path d="M0 0l7 6 7-6" fill="none" stroke="#2f2f2f" stroke-width="1.3"/></svg>hello@korvalepest.com</li>
    </ul>
  </div>
  <div class="col news" style="left:820px">
    <h5>Newsletter</h5>
    <p>Get daily tips to help reduce pest and worms.</p>
    <div class="subscribe"><span>Enter Your Email Address</span><b><svg width="14" height="11" viewBox="0 0 14 11"><rect width="14" height="11" fill="#2f2f2f"/><path d="M0 0l7 6 7-6" fill="none" stroke="#fff" stroke-width="1.3"/></svg></b></div>
  </div>
  <div class="rule"></div>
  <div class="copy">© 2021 Korvale Pest Solutions | All Rights Reserved</div>
</footer>

</body>
</html>
```